Bref créative
Corvane Oral Care Stationary
Corvane Oral Care
Professional
R. Lucien Dorvash, DDS, MAGD
2483 W Perrin Ave.
Ferrowind, TX 00000
dentist@qbl.zx.com
www.corvaneoralcare.com

```html
<!DOCTYPE html>
<html lang="en">
<head>
<meta charset="utf-8">
<title>Corvane Oral Care Stationery</title>
<link href="https://fonts.googleapis.com/css2?family=PT+Sans+Narrow:wght@400;700&display=swap" rel="stylesheet">
<style>
:root{
  --navy:#1d3a8e;
  --blue:#2d55b0;
  --lime:#9cc63b;
  --grey:#8a8d91;
  --faint:#e4e5e7;
  --paper:#ffffff;
  --ground:#e8e5e1;
  --ink:#4a4d52;
}
*{margin:0;padding:0;box-sizing:border-box}
html,body{width:1200px;height:463px;overflow:hidden;background:var(--ground)}
body{position:relative;font-family:"PT Sans Narrow",Arial,sans-serif;color:var(--ink)}
.piece{position:absolute;background:var(--paper);overflow:hidden;box-shadow:0 1px 3px rgba(0,0,0,.25)}
.piece svg.art{position:absolute;inset:0;width:100%;height:100%}
.brand{position:absolute;display:flex;align-items:center;gap:3px;font-weight:700;color:var(--navy);white-space:nowrap;line-height:1}
.brand .dot{border-radius:50%;background:var(--lime);flex:none}
.brand.rev{color:#fff}
.brand.rev .dot{background:#fff}
.small{position:absolute;font-size:4px;line-height:1.3;color:var(--ink);white-space:nowrap}
.small.rev{color:#fff}
.card{width:120px;height:52px;border-radius:4px}
.letter{width:282px;height:400px}
.watermark{position:absolute;left:0;right:0;top:150px;text-align:center;color:var(--faint);font-weight:700;line-height:.95}
.watermark .ring{width:120px;height:120px;border:14px solid var(--faint);border-radius:50%;margin:-100px auto 14px}
.watermark .l1{font-size:31px}
.watermark .l2{font-size:46px}
.footer{position:absolute;left:18px;bottom:14px;font-size:4.5px;line-height:1.4;color:var(--ink)}
.env{width:272px}
</style>
</head>
<body>

<!-- business cards: column one -->
<div class="piece card" style="left:20px;top:90px">
  <svg class="art" viewBox="0 0 120 52" preserveAspectRatio="none"><path d="M0 40 Q60 30 120 44 L120 52 L0 52Z" fill="var(--navy)"/><path d="M0 38 Q60 28 120 42 L120 44 Q60 31 0 41Z" fill="var(--lime)"/></svg>
  <div class="brand" style="left:8px;top:12px;font-size:7px"><span class="dot" style="width:7px;height:7px"></span>Corvane Oral Care</div>
</div>
<div class="piece card" style="left:20px;top:150px">
  <div class="brand" style="left:10px;top:12px;font-size:9px"><span class="dot" style="width:10px;height:10px"></span>Corvane<br>Oral Care</div>
  <div class="small" style="left:10px;top:38px">R. Lucien Dorvash, DDS, MAGD</div>
</div>
<div class="piece card" style="left:20px;top:212px">
  <svg class="art" viewBox="0 0 120 52" preserveAspectRatio="none"><rect x="0" y="0" width="120" height="10" fill="var(--lime)"/><rect x="0" y="10" width="120" height="4" fill="var(--navy)"/></svg>
  <div class="brand" style="left:8px;top:22px;font-size:7px"><span class="dot" style="width:7px;height:7px"></span>Corvane Oral Care</div>
</div>
<div class="piece card" style="left:20px;top:272px">
  <svg class="art" viewBox="0 0 120 52" preserveAspectRatio="none"><path d="M0 0 H120 V14 Q60 4 0 16Z" fill="var(--navy)"/><path d="M0 16 Q60 4 120 14 V17 Q60 8 0 19Z" fill="var(--lime)"/></svg>
  <div class="brand" style="left:8px;top:27px;font-size:7px"><span class="dot" style="width:7px;height:7px"></span>Corvane Oral Care</div>
</div>

<!-- business cards: column two -->
<div class="piece card" style="left:150px;top:90px">
  <svg class="art" viewBox="0 0 120 52" preserveAspectRatio="none"><path d="M0 44 Q60 36 120 46 L120 52 L0 52Z" fill="var(--lime)"/></svg>
  <div class="small" style="left:8px;top:8px;font-weight:700;font-size:5px;color:var(--navy)">R. Lucien Dorvash, DDS, MAGD</div>
  <div class="small" style="left:8px;top:16px">2483 W Perrin Ave.<br>Ferrowind, TX 00000<br>dentist@qbl.zx.com<br>www.corvaneoralcare.com</div>
  <div class="brand" style="left:80px;top:8px;font-size:5px"><span class="dot" style="width:5px;height:5px"></span>COC</div>
</div>
<div class="piece card" style="left:150px;top:150px;background:var(--navy)">
  <svg class="art" viewBox="0 0 120 52" preserveAspectRatio="none"><defs><radialGradient id="glow" cx="30%" cy="50%" r="60%"><stop offset="0" stop-color="var(--blue)"/><stop offset="1" stop-color="var(--navy)"/></radialGradient></defs><rect width="120" height="52" fill="url(#glow)"/></svg>
  <div class="brand rev" style="left:12px;top:15px;font-size:9px"><span class="dot" style="width:10px;height:10px"></span>Corvane<br>Oral Care</div>
</div>
<div class="piece card" style="left:150px;top:212px">
  <svg class="art" viewBox="0 0 120 52" preserveAspectRatio="none"><rect y="40" width="120" height="4" fill="var(--lime)"/><rect y="44" width="120" height="8" fill="var(--navy)"/></svg>
  <div class="small" style="left:8px;top:8px;font-weight:700;font-size:5px;color:var(--navy)">R. Lucien Dorvash, DDS</div>
  <div class="small" style="left:8px;top:16px">2483 W Perrin Ave.<br>Ferrowind, TX 00000<br>dentist@qbl.zx.com</div>
</div>
<div class="piece card" style="left:150px;top:272px">
  <svg class="art" viewBox="0 0 120 52" preserveAspectRatio="none"><g fill="var(--navy)"><rect x="50" y="8" width="70" height="3"/><rect x="50" y="14" width="70" height="3"/><rect x="50" y="20" width="70" height="3"/></g><rect x="50" y="26" width="70" height="3" fill="var(--lime)"/></svg>
  <div class="brand" style="left:8px;top:10px;font-size:6px"><span class="dot" style="width:6px;height:6px"></span>COC</div>
  <div class="small" style="left:8px;top:34px">dentist@qbl.zx.com · www.corvaneoralcare.com</div>
</div>

<!-- letterhead one -->
<div class="piece letter" style="left:312px;top:52px">
  <svg class="art" viewBox="0 0 282 400" preserveAspectRatio="none"><defs><linearGradient id="band" x1="0" x2="1"><stop offset="0" stop-color="var(--lime)"/><stop offset=".55" stop-color="var(--lime)"/><stop offset="1" stop-color="var(--navy)"/></linearGradient></defs><path d="M0 0 H282 V22 Q140 6 0 12Z" fill="url(#band)"/><path d="M0 392 H282 V400 H0Z" fill="var(--lime)"/></svg>
  <div class="brand" style="left:18px;top:26px;font-size:13px"><span class="dot" style="width:14px;height:14px"></span>Corvane<br>Oral Care</div>
  <div class="watermark"><div class="ring"></div><div class="l1">Corvane Oral</div><div class="l2">CARE</div></div>
  <div class="footer">2483 W Perrin Ave. · Ferrowind, TX 00000 · Phone 000.555.0142<br>dentist@qbl.zx.com · www.corvaneoralcare.com</div>
</div>

<!-- letterhead two -->
<div class="piece letter" style="left:620px;top:52px">
  <svg class="art" viewBox="0 0 282 400" preserveAspectRatio="none"><rect x="12" y="14" width="120" height="3" fill="var(--navy)"/><rect x="140" y="14" width="130" height="3" fill="var(--lime)"/><rect x="0" y="374" width="140" height="10" fill="var(--lime)"/><rect x="140" y="374" width="142" height="10" fill="var(--navy)"/></svg>
  <div class="brand" style="left:18px;top:26px;font-size:13px"><span class="dot" style="width:14px;height:14px"></span>Corvane<br>Oral Care</div>
  <div class="watermark"><div class="ring"></div><div class="l1">Corvane Oral</div><div class="l2">CARE</div></div>
  <div class="footer" style="bottom:28px;left:150px">2483 W Perrin Ave. · Ferrowind, TX 00000<br>dentist@qbl.zx.com · www.corvaneoralcare.com</div>
</div>

<!-- envelope one -->
<div class="piece env" style="left:910px;top:82px;height:110px">
  <svg class="art" viewBox="0 0 272 110" preserveAspectRatio="none"><defs><linearGradient id="top" x1="0" x2="1"><stop offset="0" stop-color="var(--navy)"/><stop offset=".5" stop-color="var(--lime)"/><stop offset="1" stop-color="var(--navy)"/></linearGradient></defs><rect width="272" height="14" fill="url(#top)"/><rect y="104" width="272" height="6" fill="var(--lime)"/></svg>
  <div class="brand" style="left:12px;top:22px;font-size:7px"><span class="dot" style="width:8px;height:8px"></span>Corvane<br>Oral Care</div>
</div>

<!-- envelope two -->
<div class="piece env" style="left:910px;top:228px;height:40px">
  <svg class="art" viewBox="0 0 272 40" preserveAspectRatio="none"><rect x="0" y="6" width="272" height="2" fill="var(--navy)"/><rect x="0" y="10" width="272" height="2" fill="var(--lime)"/></svg>
  <div class="brand" style="left:170px;top:16px;font-size:8px"><span class="dot" style="width:8px;height:8px"></span>Corvane Oral Care</div>
</div>

<!-- envelope three -->
<div class="piece env" style="left:910px;top:288px;height:52px">
  <svg class="art" viewBox="0 0 272 52" preserveAspectRatio="none"><path d="M0 0 H272 V10 Q140 2 0 16Z" fill="var(--navy)"/><path d="M0 16 Q140 2 272 10 V13 Q140 6 0 19Z" fill="var(--lime)"/></svg>
  <div class="brand" style="left:12px;top:26px;font-size:7px"><span class="dot" style="width:7px;height:7px"></span>Corvane Oral Care</div>
</div>

<!-- envelope four -->
<div class="piece env" style="left:910px;top:352px;height:54px">
  <svg class="art" viewBox="0 0 272 54" preserveAspectRatio="none"><g fill="var(--navy)"><rect x="130" y="10" width="142" height="3"/><rect x="130" y="17" width="142" height="3"/><rect x="130" y="24" width="142" height="3"/></g><rect x="130" y="31" width="142" height="3" fill="var(--lime)"/></svg>
  <div class="brand" style="left:12px;top:10px;font-size:7px"><span class="dot" style="width:7px;height:7px"></span>Corvane Oral Care</div>
  <div class="small" style="left:12px;top:24px">2483 W Perrin Ave.<br>Ferrowind, TX 00000</div>
</div>

</body>
</html>
```